Q7 Halvern needs an A4 folding brochure

We need a new 3-page, A4 folding brochure for Q7 Halvern, an expansion of Q7 Engineering Pty Ltd (www.q7engineering.com.au).

We provide high quality professional services for the Australian space industry. Our clients include the Dunmore Federal Bureau and companies working in the space industry. We identify people with space related skills both locally and internationally who are then contracted by clients to create products and support space launch activities.

We would like the brochure to be based on an A4 page (landscape, folded into 3 sections) and look technical with a particular focus on communications systems, satellites, launchpad technology, space situational awareness, and Internet-of-Things (IoT) technology being developed within the space industry. The brochure will be provided to potential space customers and should be professional, visually appealing, clear, and uncluttered.

Include the Q7 Halvern logo and the Q7 Halvern heading (both are attached)

Include pictures (Australian preferred) of mission control centres, rockets, satellites, radio communications equipment, large satellite dishes, night landscapes with stars, or pictures of Australia or Earth from space. Include both graphics and photos. No cartoons or space shuttles from the 1980s please. Images should be current rather than old.

Include text from the attached ‘Q7 Halvern – brochure text’ file.

We would like the colours to match the Q7 Halvern logo, using mainly: navy blue (#000080) and matching blues; platinum (#E5E4E2), rocket metallic (#8A7F8D) and similar greys; black (#000000), and white (#FFFFFF). Sunlight colours may be included sparingly as a highlight.

Attached files:
- I have attached the Q7 Halvern logo which must appear on the brochure (‘q7halvern.ai’)
- I have attached the Q7 Halvern heading, which should also appear on the brochure (‘q7halvern-heading.psd’)
- I have attached the text that must be included on the brochure. Please divide this over the pages according to how it is group on the attached document. (‘Q7 Halvern – brochure text’)

The following organisation logos are also attached, to be included on the brochure:
- Brackwell Trade Guild - Member (‘BTG_member_logo_72’)
- Dunmore Federal Bureau – Supplier (‘DFBSupplier’)
- Fennick Society Inc. (‘FS_160x160’)

Target Market(s)

Our clients include the Dunmore Federal Bureau and companies working in the space industry within Australia and internationally.

Requirements
Must have
• Refer to specifications in the project description above.
Nice to have
Should not have

```html
<!DOCTYPE html>
<html lang="en">
<head>
<meta charset="utf-8">
<title>Q7 Halvern – Tri-fold Brochure</title>
<link rel="stylesheet" href="https://fonts.googleapis.com/css2?family=Roboto:wght@400;500;700&family=Roboto+Condensed:wght@400;700&display=swap">
<style>
:root{
  --navy:#22236c;
  --navy-deep:#15164f;
  --navy-bright:#2f3190;
  --platinum:#e5e4e2;
  --metal:#8a7f8d;
  --ink:#2b2b3a;
  --white:#ffffff;
  --bg:#d9d9d9;
  --photo-dark:#141d4a;
  --photo-mid:#2c4380;
  --photo-light:#5d7cbb;
}
*{box-sizing:border-box;margin:0;padding:0}
html,body{width:851px;height:1200px;overflow:hidden;background:var(--bg)}
body{font-family:"Roboto",Arial,sans-serif;color:var(--ink);position:relative}
.spread{position:absolute;left:10px;width:831px;height:584px;background:var(--white);overflow:hidden;box-shadow:0 3px 8px rgba(0,0,0,.18)}
.spread--outside{top:12px}
.spread--inside{top:606px}
.panel{position:absolute;top:0;height:100%;width:277px}
.panel--left{left:0}
.panel--mid{left:277px;width:281px;background:linear-gradient(180deg,var(--navy-bright),var(--navy) 45%,var(--navy-deep))}
.panel--right{left:558px;width:273px}
.abs{position:absolute}
.photo{position:absolute}
h2.lead{font-family:"Roboto Condensed",Arial,sans-serif;font-weight:700;color:var(--navy);font-size:10.5px;line-height:1.25}
p.body{font-size:6.6px;line-height:1.3;text-align:justify;color:#3a3a48}
.ticks{list-style:none}
.ticks li{position:relative;padding-left:14px;font-size:6.6px;line-height:1.25;margin-bottom:5px;color:#3a3a48}
.ticks li::before{content:"";position:absolute;left:0;top:0;width:7px;height:7px;border:1px solid var(--metal);border-radius:50%}
.ticks li::after{content:"";position:absolute;left:2.5px;top:1.6px;width:2px;height:3.5px;border:solid var(--metal);border-width:0 1px 1px 0;transform:rotate(45deg)}
.ticks--light li{color:#e9e9f5;margin-bottom:3.4px}
.ticks--light li::before{border-color:#b9b9d8}
.ticks--light li::after{border-color:#b9b9d8}
.wordmark{font-family:"Roboto",Arial,sans-serif;font-weight:400;color:var(--white);letter-spacing:9px;font-size:22px;text-align:center;width:100%}
.wordmark-dot{display:inline-block;width:14px;height:14px;border-radius:50%;background:var(--white);margin-right:10px;vertical-align:1px}
.bar{position:absolute;background:var(--metal);color:var(--white);font-size:11px;text-align:center;clip-path:polygon(3% 0,100% 0,97% 100%,0 100%)}
.contact{color:var(--white);text-align:center;width:100%;font-size:10.5px;line-height:1.45}
.badge{position:absolute;top:0;border-radius:50%}
.mid-head{font-family:"Roboto Condensed",Arial,sans-serif;color:var(--white);font-size:10px;letter-spacing:.3px}
.ring{position:absolute;width:30px;height:30px;border-radius:50%;border:2px solid #9a9ac6;background:var(--navy-deep)}
.icon-box{position:absolute;left:0;width:18px;height:18px;border:1.4px solid var(--navy);border-radius:4px}
.svc{position:absolute;left:18px;width:250px;font-size:6.8px;line-height:1.25;color:#3a3a48}
.svc span{display:block;padding-left:26px;min-height:20px}
.rule{border-bottom:1px dashed #c9c9d3;margin-bottom:7px;padding-bottom:5px}
.mission{position:absolute;left:17px;width:250px;top:497px;height:42px;background:var(--navy);color:var(--white);border-radius:3px;font-size:8.2px;text-align:center;line-height:1.45;padding-top:7px;letter-spacing:.2px}
</style>
</head>
<body>

<section class="spread spread--outside">

  <div class="panel panel--left">
    <h2 class="lead abs" style="left:17px;top:16px;width:255px">Are you living outside of Australia and want to work within Australia’s dynamic and evolving Space sector?</h2>
    <p class="body abs" style="left:17px;top:46px;width:254px">Q7 Halvern provides a streamlined process, support services, and employment options to suitably qualified people who are seeking work within Space in Australia.</p>
    <p class="body abs" style="left:17px;top:78px;width:254px">Our transition plans include flexible employment options, relocation services to accommodate your needs, remote work options, ongoing assistance, and valuable local information to empower you to navigate your time in Australia with ease. Our mission is to bring exceptional talent into the Australian Space sector and offer a quality experience that is both enjoyable and rewarding.</p>
    <p class="body abs" style="left:17px;top:134px;width:254px">If you’re an experienced Space professional seeking to work within Australia, contact us at enquiries@q7halvern.com.au.</p>
    <h2 class="lead abs" style="left:17px;top:162px;width:255px">Q7 Halvern is an agile, open, flexible professional service innovator.</h2>
    <ul class="ticks abs" style="left:17px;top:192px;width:254px">
      <li>We are adaptable to your requirements.</li>
      <li>We can source personnel across a wide range of specialisations and skill levels.</li>
      <li>We are flexible in developing the teams you need to get the job done well.</li>
      <li>We deliver solutions to your resourcing problems.</li>
    </ul>
    <p class="body abs" style="left:17px;top:260px;width:254px">At Q7 Halvern, we are committed to delivering value to all our clients and end users in a manner that inspires.</p>
    <div class="abs" style="left:34px;top:282px;width:230px;height:40px" aria-label="Partner badges: Fennick Society Inc., Dunmore Federal Bureau supplier, Brackwell Trade Guild member" role="img">
      <div class="badge" style="left:0;width:36px;height:36px;border:2px solid #555;background:var(--platinum)"></div>
      <div class="badge" style="left:62px;top:6px;width:78px;height:24px;border-radius:4px;background:#c9cbe0"></div>
      <div class="badge" style="left:155px;top:7px;width:58px;height:22px;border-radius:4px;background:#9fb2d9"></div>
    </div>
    <svg class="photo" style="left:0;top:330px" width="277" height="254" viewBox="0 0 277 254" role="img" aria-label="Photo of a large radio telescope dish">
      <defs><linearGradient id="dishFill" x1="0" y1="0" x2="1" y2="1"><stop offset="0" stop-color="var(--photo-mid)"/><stop offset="1" stop-color="var(--photo-light)"/></linearGradient></defs>
      <path d="M0 30 Q140 -10 277 60 L277 254 L0 254 Z" fill="var(--navy)"/>
      <path d="M0 40 Q140 2 277 72 L277 254 L0 254 Z" fill="url(#dishFill)"/>
    </svg>
  </div>

  <div class="panel panel--mid">
    <div class="abs" style="top:300px;left:0;width:100%"><div class="wordmark"><span class="wordmark-dot"></span>Q7 HALVERN</div></div>
    <p class="abs" style="top:360px;left:10px;width:261px;text-align:center;color:#c9c9dd;font-size:8px;line-height:1.6">EXCELLENCE, INTEGRITY, AND QUALITY OF SERVICE<br>ARE OUR HIGHEST PRIORITIES.</p>
    <div class="bar" style="left:57px;top:402px;width:166px;height:18px;line-height:18px">CONTACT US</div>
    <p class="contact abs" style="top:431px">General Enquiries: enquiries@q7halvern.com.au<br>Career Opportunities: careers@q7halvern.com.au</p>
    <p class="contact abs" style="top:479px">Main Office Level 4, 18 Carrow St<br>Eastbury VIC 3288</p>
    <p class="contact abs" style="top:520px;font-size:15px;letter-spacing:.6px">www.Q7Halvern.com.au</p>
    <p class="abs" style="top:549px;left:14px;width:253px;text-align:center;color:#8f90b8;font-size:5.4px;line-height:1.5">Q7 Halvern is the registered trading name of Q7 Engineering Pty Ltd ABN 00 321 654 987 located at Level 4, 18 Carrow St, Eastbury 3288.</p>
  </div>

  <div class="panel panel--right">
    <div class="abs" style="left:0;top:413px;width:100%;text-align:center;font-family:'Roboto',Arial,sans-serif;font-weight:700;color:var(--navy);font-size:27px;letter-spacing:4px">Q7 HALVERN</div>
    <div class="abs" style="left:0;top:494px;width:100%;text-align:center;font-family:'Roboto Condensed',Arial,sans-serif;font-weight:700;color:var(--navy);font-size:17.5px;letter-spacing:.4px">DELIVERING EXCELLENCE</div>
    <p class="abs" style="left:0;top:519px;width:100%;text-align:center;color:var(--metal);font-size:10.5px;line-height:1.3">A trusted provider to the world’s<br>most exacting clients</p>
    <div class="abs" style="left:35px;top:555px;width:228px;height:20px;background:var(--navy);clip-path:polygon(2% 0,100% 0,98% 100%,0 100%);color:var(--white);font-size:11px;line-height:20px;letter-spacing:.5px">
      <svg style="position:absolute;left:22px;top:5px" width="10" height="10" viewBox="0 0 10 10"><circle cx="5" cy="5" r="4.3" fill="none" stroke="#fff" stroke-width="1.1"/><path d="M.7 5h8.6M5 .7c-2.3 2.4-2.3 6.2 0 8.6M5 .7c2.3 2.4 2.3 6.2 0 8.6" fill="none" stroke="#fff" stroke-width=".8"/></svg>
      <span style="position:absolute;left:44px">www.Q7Halvern.com.au</span>
    </div>
  </div>

  <svg class="photo" style="left:277px;top:0" width="554" height="380" viewBox="0 0 554 380" role="img" aria-label="Photo of Earth from space showing Australia">
    <defs><linearGradient id="earthFill" x1="0" y1="0" x2="1" y2="1"><stop offset="0" stop-color="var(--photo-dark)"/><stop offset="1" stop-color="var(--photo-mid)"/></linearGradient></defs>
    <path d="M220 0 L554 0 L554 330 Q430 378 330 330 Q240 260 220 0 Z" fill="var(--navy)"/>
    <path d="M232 0 L554 0 L554 316 Q430 360 335 318 Q250 250 232 0 Z" fill="url(#earthFill)"/>
  </svg>
  <svg class="photo" style="left:343px;top:80px" width="124" height="124" viewBox="0 0 124 124" role="img" aria-label="Photo of a satellite orbiting above Earth">
    <circle cx="62" cy="62" r="61" fill="var(--white)"/>
    <circle cx="62" cy="62" r="57" fill="var(--photo-light)"/>
  </svg>
</section>

<section class="spread spread--inside">

  <div class="panel panel--left">
    <svg class="photo" style="left:0;top:0" width="300" height="240" viewBox="0 0 300 240" role="img" aria-label="Photo of engineers in a mission control room facing large screens">
      <defs><linearGradient id="ctrlFill" x1="0" y1="0" x2="1" y2="1"><stop offset="0" stop-color="var(--photo-dark)"/><stop offset="1" stop-color="var(--photo-mid)"/></linearGradient></defs>
      <path d="M0 0 L290 0 Q310 150 220 215 Q140 250 0 214 Z" fill="var(--navy)"/>
      <path d="M0 0 L278 0 Q296 140 214 205 Q140 238 0 204 Z" fill="url(#ctrlFill)"/>
    </svg>
    <h2 class="lead abs" style="left:17px;top:257px;width:260px">Q7 Halvern provides solutions to critical Space-sector challenges through professional services, including:</h2>
    <div class="svc" style="top:296px">
      <div class="rule"><i class="icon-box"></i><span>Providing specialist Space-industry personnel with management, publications, and technical skills</span></div>
      <div class="rule"><i class="icon-box"></i><span>Technical consultancy services</span></div>
      <div><i class="icon-box"></i><span>Project delivery</span></div>
    </div>
    <h2 class="lead abs" style="left:17px;top:390px;font-size:9.4px">We operate both nationally and internationally:</h2>
    <div class="svc" style="top:413px">
      <div class="rule"><i class="icon-box" style="border-radius:2px"></i><span>Nationally, we deliver the right people for the project results you need.</span></div>
      <div><i class="icon-box" style="border-radius:50%"></i><span>Internationally, we source highly skilled space professionals to increase your competitive edge in a rapidly expanding market.</span></div>
    </div>
    <div class="mission">OUR MISSION IS TO BRING EXCEPTIONAL TALENT<br>INTO THE AUSTRALIAN SPACE SECTOR.</div>
    <p class="abs" style="left:17px;top:552px;width:250px;text-align:center;font-size:7.4px;line-height:1.35;color:#222">Contact us at enquiries@q7halvern.com.au<br>with your project needs</p>
  </div>

  <div class="panel panel--mid">
    <div class="abs" style="top:52px;left:0;width:100%"><div class="wordmark"><span class="wordmark-dot"></span>Q7 HALVERN</div></div>
    <div class="bar" style="left:18px;top:101px;width:246px;height:19px;line-height:19px;font-size:10px">Key enabler to the Space industry sector</div>
    <p class="abs" style="left:20px;top:131px;width:241px;text-align:center;color:#c4c5df;font-size:6.8px;line-height:1.35">Our services aim to fast-track project development, pre-empt and solve problems more efficiently, and inspire and guide success. By delivering expertise and talent we help businesses convert possibilities into reality and build their customer confidence.</p>
    <p class="abs" style="left:20px;top:212px;color:var(--white);font-size:7.5px;font-weight:500">Q7 Halvern can supply your project and tasking needs for:</p>

    <span class="ring" style="left:20px;top:240px"></span>
    <div class="abs" style="left:68px;top:247px">
      <div class="mid-head">MANAGEMENT</div>
      <ul class="ticks ticks--light" style="margin-top:4px">
        <li>Project Management</li><li>Risk Analysis</li><li>Scheduling</li>
        <li>Data Configuration Management (CM)</li><li>Process Definition and Improvement (Quality)</li>
      </ul>
    </div>

    <span class="ring" style="left:20px;top:340px"></span>
    <div class="abs" style="left:68px;top:346px">
      <div class="mid-head">PUBLICATION</div>
      <ul class="ticks ticks--light" style="margin-top:4px">
        <li>General Authoring</li><li>Technical Authoring</li>
      </ul>
    </div>

    <span class="ring" style="left:20px;top:406px"></span>
    <div class="abs" style="left:68px;top:411px">
      <div class="mid-head">TECHNICAL SPECIALISTS (SPACE)</div>
      <ul class="ticks ticks--light" style="margin-top:4px">
        <li>Systems and Software</li><li>Safety</li><li>Satellite Systems</li><li>Mechanical</li>
        <li>Radio (RF) Communications</li><li>System Integration</li><li>Electrical/Power</li>
        <li>Aerospace</li><li>Technology Security (Cyber)</li><li>Networking</li><li>Communications (Data)</li>
      </ul>
    </div>
  </div>

  <div class="panel panel--right">
    <h2 class="lead abs" style="left:14px;top:30px;font-weight:400;font-size:10.5px">Specialised support service provider</h2>
    <div class="abs" style="left:14px;top:52px;width:252px">
      <p class="body" style="margin-bottom:9px">Q7 Halvern personnel have been at the forefront of major program deliveries to Defence and Commercial sector clients for decades. Our staff are leaders in their field and pioneers in the establishment of systematic approaches to the most complex problems.</p>
      <p class="body" style="margin-bottom:9px">With access to skilled personnel locally and internationally, Q7 Halvern can review, de-risk, and support delivery of space orientated systems and services.</p>
      <p class="body" style="margin-bottom:9px">Q7 Halvern is supported by engineers with capabilities in the design and development of rocket systems and expertise in RF SATCOM communications technologies.</p>
      <p class="body" style="margin-bottom:9px">We understand rocket systems from work on missile and UAV development and trials at Woomera, Jervis Bay, RAN ships, and Port Wakefield test range.</p>
      <p class="body" style="margin-bottom:9px">We understand the complexity associated with launch facilities, rocket launch, and recovery operations for rocket propelled systems and associated technologies.</p>
      <p class="body" style="margin-bottom:9px">We understand cybersecurity technologies, communications, systems engineering, systems design, facilities, integration, infrastructure, and modern systems development principles. And by understanding, we are in the best position to support our customer requirements and business needs.</p>
      <p class="body">With prior work on multi-billion-dollar programs of tactical and strategic importance to the country, we can directly support the Space sector in education, research and technology development that helps grow the broader community interest in space.</p>
    </div>
  </div>

  <svg class="photo" style="left:520px;top:370px" width="311" height="214" viewBox="0 0 311 214" role="img" aria-label="Illustration of a rocket and satellites above Earth">
    <defs><linearGradient id="rocketFill" x1="0" y1="0" x2="1" y2="1"><stop offset="0" stop-color="var(--photo-dark)"/><stop offset="1" stop-color="var(--photo-mid)"/></linearGradient></defs>
    <path d="M38 214 Q10 90 70 40 Q170 -10 311 18 L311 214 Z" fill="var(--navy)"/>
    <path d="M48 214 Q22 96 80 50 Q175 2 311 30 L311 214 Z" fill="url(#rocketFill)"/>
  </svg>
</section>

</body>
</html>
```